Instagram background for quotes

We need a 1080x1080 background for instagram. I use the Phonto app to put text over the image.

We create motivating and inspiring messages for our followers on IG.

Our brands message is, "Mediocre thinking leads to mediocre results. Get Mission - Get Motivated - Get Moving
https://www.example-social.test/steel_resolve_co/

We would like to move away from the rustic look and have a gloss black background with the goal of using text that is cleaner to match the SR in the logo.

I see the design remaining fairly close to what it is now with the logo at the top. I like the quotes on this brand here, https://www.example-social.test/talkwithtycoons/?hl=en. I see this being built into our new background with the quotations being aggressive to match the wings in our logo.

Here is another brand we like - https://www.example-social.test/boomboomdrive/

I've attached the files I was given by the logo designer who has disappeared. I am hoping what is there will suffice.

Target Market(s)

24-34 year old males

Industry/Entity Type

Quotes

Colors
000000
ffffff

Requirements
Must have
• Provided Logo without text
Nice to have
• Aggressive looking quotes to match wings
• Watermark logo in background

```html
<!DOCTYPE html>
<html lang="en">
<head>
<meta charset="utf-8">
<title>Steel Resolve — Quote Background</title>
<link rel="stylesheet" href="https://fonts.googleapis.com/css2?family=Anton&family=Archivo+Black&family=Orbitron:wght@600&display=swap">
<style>
  :root {
    --page: #ffffff;
    --panel: #000000;
    --ink: #ffffff;
    --panel-edge: #3a3a3a;
    --ghost: rgba(255, 255, 255, 0.1);
  }
  html, body {
    margin: 0;
    padding: 0;
    width: 1200px;
    height: 1200px;
    overflow: hidden;
    background: var(--page);
  }
  .canvas {
    display: block;
    width: 1200px;
    height: 1200px;
  }
  .panel { fill: var(--panel); stroke: var(--panel-edge); stroke-width: 2; }
  .brand-name {
    font-family: "Archivo Black", sans-serif;
    font-size: 130px;
    fill: var(--ink);
  }
  .brand-ghost {
    font-family: "Archivo Black", sans-serif;
    font-size: 300px;
    fill: var(--ghost);
  }
  .quote-frame { fill: none; stroke: var(--ink); stroke-width: 2.5; }
  .quote-mark {
    font-family: "Anton", sans-serif;
    font-size: 230px;
    fill: var(--ink);
  }
  .quote-text {
    font-family: "Archivo Black", sans-serif;
    font-size: 58px;
    fill: var(--ink);
  }
  .hashtag {
    font-family: "Orbitron", sans-serif;
    font-weight: 600;
    font-size: 30px;
    fill: var(--ink);
  }
</style>
</head>
<body>
<svg class="canvas" viewBox="0 0 1200 1200" xmlns="http://www.w3.org/2000/svg">
  <rect class="panel" x="194" y="194" width="840" height="840"/>

  <!-- brand name at top -->
  <text class="brand-name" x="613" y="380" text-anchor="middle">SR</text>

  <!-- faint brand name behind the quote -->
  <text class="brand-ghost" x="640" y="745" text-anchor="middle">SR</text>

  <!-- quote frame -->
  <path class="quote-frame" d="M366 500 H954 V734"/>
  <path class="quote-frame" d="M274 534 V772 H862"/>

  <!-- quote marks -->
  <text class="quote-mark" x="248" y="640">“</text>
  <text class="quote-mark" x="884" y="930">”</text>

  <!-- quote -->
  <text class="quote-text" x="617" y="584" text-anchor="middle" textLength="538" lengthAdjust="spacingAndGlyphs">don’t allow other</text>
  <text class="quote-text" x="623" y="656" text-anchor="middle" textLength="538" lengthAdjust="spacingAndGlyphs">people to dictate</text>
  <text class="quote-text" x="618" y="728" text-anchor="middle" textLength="484" lengthAdjust="spacingAndGlyphs">your emotions.</text>

  <!-- hashtag -->
  <text class="hashtag" x="613" y="990" text-anchor="middle" textLength="458" lengthAdjust="spacingAndGlyphs">#STEELRESOLVE</text>
</svg>
</body>
</html>
```